Vereda 14

Executive Corporate Housing Presentation (B2B Mobility Asset)
We are creating a Corporate Serviced Residence Pitch Deck for international corporate clients (e.g. Brivanta, global mobility teams, relocation departments).
The document is not a traditional real estate brochure. It is a B2B operational housing presentation designed for procurement, HR and corporate mobility decision-makers.
OBJECTIVE
The goal is to communicate:
Operational clarity
Corporate compliance readiness
Location feasibility
Building structure and usability
Executive-level accommodation standard
Reduced relocation and HR friction
DESIGN STYLE
The visual identity should be:
Clean corporate (Thackery / Vantrelle / Brivanta style)
Minimalist, high whitespace
Structured and modular (not emotional storytelling)
Data + diagram driven
Subtle luxury (not hospitality marketing)
🚫AVOID
Real estate marketing style
Nestiqo / hospitality visuals
Overly emotional language or lifestyle imagery
Cluttered property listings
Dense technical architectural drawings
KEY VISUAL ELEMENT
Strong emphasis on:
Simplified building diagrams (hotel-style mapping)
Flow-based visuals (how users move through the building)
Corporate icons (access, parking, units, workspace)
Modular information blocks
DESIGN INTENT
The document should feel like:
“A corporate mobility solution presentation”
not
“a luxury property brochure”
Document will be around 12 pages long, I will provide all text and pictures. Enclosed an idea of the desired style. It has to be possible to make changes in the document (PDF - change renders to pictures & change the company's name if needed)
International corporate clients

```html
<!DOCTYPE html>
<html lang="en">
<head>
<meta charset="utf-8">
<title>Vereda 14 — Executive Corporate Housing</title>
<link rel="stylesheet" href="https://fonts.googleapis.com/css2?family=Newsreader:opsz,wght@6..72,400&family=Poppins:wght@400;500&family=Outfit:wght@400&display=swap">
<style>
  :root{
    --board:#aba8a7;
    --paper:#ffffff;
    --panel:#f3f1ec;
    --ink:#151515;
    --muted:#6d6d6d;
    --olive:#5f5a25;
    --line:#d9d5c2;
    --icon-bg:#ebeae6;
    --serif:"Newsreader", Georgia, serif;
    --sans:"Poppins", Arial, sans-serif;
    --caps:"Outfit", Arial, sans-serif;
  }
  *{box-sizing:border-box;margin:0;padding:0}
  html,body{width:1200px;height:715px;overflow:hidden;background:var(--board)}
  body{position:relative;font-family:var(--sans);color:var(--ink)}
  .slide{position:absolute;background:var(--paper);overflow:hidden}
  .slide--cover{left:46px;top:43px;width:534px;height:300px}
  .slide--summary{left:618px;top:43px;width:535px;height:300px}
  .slide--why{left:333px;top:369px;width:534px;height:300px}

  /* cover */
  .cover__emblem{position:absolute;left:125px;top:34px;width:44px;height:44px;border-radius:50%;background:var(--icon-bg)}
  .cover__title{position:absolute;left:0;width:308px;top:91px;text-align:center;font-family:var(--serif);font-size:35px;letter-spacing:.5px;font-weight:400;line-height:42px}
  .cover__subtitle{position:absolute;left:0;width:308px;top:132px;text-align:center;font-family:var(--caps);font-size:10.5px;letter-spacing:1.3px;color:var(--olive)}
  .cover__pillars{position:absolute;left:38px;top:165px;display:flex}
  .pillar{width:75px;text-align:center;font-size:7.5px;line-height:11.5px}
  .pillar svg{display:block;margin:0 auto 6px;height:28px}
  .pillar--divided{border-left:1px solid var(--line)}
  .cover__band{position:absolute;left:0;width:308px;top:255px;height:22px;border-top:1px solid #bdbdbd;border-bottom:1px solid #bdbdbd;display:flex;align-items:center;justify-content:center;font-family:var(--caps);font-size:7.6px;letter-spacing:.6px;color:var(--muted)}
  .cover__photo{position:absolute;left:308px;top:0;width:226px;height:300px;background:linear-gradient(180deg,#d6dfe6 0%,#e4ddd2 28%,#d8cfc1 60%,#8f877b 100%)}

  /* shared */
  .tag{position:absolute;border:1px solid var(--olive);color:var(--olive);font-family:var(--caps);font-size:8px;letter-spacing:2px;padding:1px 3px 0 4px;line-height:11px}
  .heading{font-family:var(--serif);font-weight:400}
  .rule{position:absolute;height:1px;width:17px;background:var(--olive)}
  .footer{position:absolute;top:273px;font-size:6.8px;color:#333}
  .page-no{position:absolute;top:274px;font-size:6.8px;color:#333}

  /* summary */
  .summary .tag{left:30px;top:30px}
  .summary__heading{position:absolute;left:30px;top:52px;width:240px;font-size:16.6px;line-height:23px}
  .summary .rule{left:30px;top:127px}
  .summary__body{position:absolute;left:30px;top:137px;width:226px;font-size:8.4px;line-height:13.7px}
  .summary__lead{position:absolute;left:31px;top:203px;width:232px;font-size:8.4px;line-height:13.7px;font-weight:500}
  .summary__panel{position:absolute;left:345px;top:0;width:190px;height:300px;background:var(--panel)}
  .benefit{position:absolute;left:18px;display:flex;align-items:center}
  .benefit__icon{width:31px;height:31px;border-radius:50%;border:1px solid #cfcac0;background:#fff;display:flex;align-items:center;justify-content:center;margin-right:12px;flex:none}
  .benefit__text{font-size:8.3px;line-height:13.7px}

  /* why */
  .why .tag{left:50%;transform:translateX(-50%);top:30px}
  .why__heading{position:absolute;left:0;width:100%;top:48px;text-align:center;font-size:16.6px}
  .why .rule{left:248px;top:76px}
  .features{position:absolute;left:30px;width:474px;border:1px solid var(--line);display:flex;padding:8px 0}
  .features--top{top:89px;height:80px}
  .features--bottom{top:174px;height:76px}
  .feature{flex:1;display:flex;flex-direction:column;align-items:center;text-align:center;font-size:8.3px;line-height:11.6px;padding-top:1px}
  .feature + .feature{border-left:1px solid var(--line)}
  .feature svg{height:28px;margin-bottom:10px}
  .why .footer{left:30px}
  .why .page-no{right:30px}
  .summary .footer{left:30px}
  .summary .page-no{left:496px}
  svg .s{fill:none;stroke:var(--olive);stroke-width:1;stroke-linecap:round;stroke-linejoin:round}
  svg .g{fill:none;stroke:#555;stroke-width:1;stroke-linecap:round;stroke-linejoin:round}
</style>
</head>
<body>

<section class="slide slide--cover">
  <span class="cover__emblem"></span>
  <h1 class="cover__title">VEREDA 14</h1>
  <p class="cover__subtitle">EXECUTIVE CORPORATE HOUSING</p>
  <div class="cover__pillars">
    <div class="pillar">
      <svg width="32" height="28" viewBox="0 0 32 28"><g class="g"><path d="M2 13L16 2l14 11M6 10v16h20V10M21 4h3v4"/><path d="M16 22l-5-5a3 3 0 0 1 5-3 3 3 0 0 1 5 3z"/></g></svg>
      Move-in Really<br>Comfort
    </div>
    <div class="pillar pillar--divided">
      <svg width="32" height="28" viewBox="0 0 32 28"><g class="g"><path d="M16 3l2 4 4 .5-3 3 .8 4-3.8-2-3.8 2 .8-4-3-3 4-.5z"/><path d="M3 10l2 9 6 6M29 10l-2 9-6 6M8 14l4 4M24 14l-4 4"/></g></svg>
      Effortless<br>Living
    </div>
    <div class="pillar pillar--divided">
      <svg width="32" height="28" viewBox="0 0 32 28"><g class="g"><circle cx="16" cy="6" r="3"/><path d="M16 1v1M11 6h1M20 6h1M16 11v3M6 17l10-4 10 4-10 4zM6 17v7l10 4 10-4v-7M16 21v7"/></g></svg>
      Curated fur<br>Professionals
    </div>
  </div>
  <div class="cover__band">Corporate Serviced Residences For Global Mobility Teams</div>
  <div class="cover__photo" role="img" aria-label="Photograph of the restored 1908 white stone corner residence with wrought-iron balconies against a pale sky"></div>
</section>

<section class="slide slide--summary summary">
  <span class="tag">EXECUTIVE SUMMARY</span>
  <h2 class="heading summary__heading">A Curated Corporate Housing Solution Designed for Global Professionals.</h2>
  <span class="rule"></span>
  <p class="summary__body">Set within a beautifully restored 1908 residence,<br>Vereda 14 offers five unique apartment designs that blend historic character with contemporary comfort and effortless move in living.</p>
  <p class="summary__lead">Your employees only need to bring their suitcases; we have taken care of everything else.</p>
  <p class="footer">© 2026 , Vereda14. All rights reserved.</p>
  <div class="summary__panel">
    <div class="benefit" style="top:55px">
      <span class="benefit__icon"><svg width="18" height="18" viewBox="0 0 18 18"><g class="g"><circle cx="11" cy="6" r="3.5"/><path d="M1 12h3l4 2h4l4-3M4 12v4M8 14l3-1"/></g></svg></span>
      <span class="benefit__text">Move-in Ready<br>fully Equipped</span>
    </div>
    <div class="benefit" style="top:101px">
      <span class="benefit__icon"><svg width="18" height="18" viewBox="0 0 18 18"><g class="g"><circle cx="6" cy="3" r="1.6"/><path d="M4 6l2 6h6l2 4M3 8l2 7h5M10 12l3-3"/></g></svg></span>
      <span class="benefit__text">Premium<br>Comfort &amp; Design</span>
    </div>
    <div class="benefit" style="top:149px">
      <span class="benefit__icon"><svg width="18" height="18" viewBox="0 0 18 18"><g class="g"><path d="M1 9l8-7 8 7M3 8v8h12V8M9 13l-2.5-2.5a1.5 1.5 0 0 1 2.5-1.5 1.5 1.5 0 0 1 2.5 1.5z"/></g></svg></span>
      <span class="benefit__text">Ideall for Short or<br>Long Stays</span>
    </div>
    <div class="benefit" style="top:198px">
      <span class="benefit__icon"><svg width="18" height="18" viewBox="0 0 18 18"><g class="g"><rect x="7" y="2" width="9" height="12" rx="1"/><path d="M9 5h5M9 8h5M9 11h3"/><circle cx="5" cy="10" r="2.5"/><path d="M2 17l1.5-3M8 17l-1.5-3"/></g></svg></span>
      <span class="benefit__text">Tailored for<br>Corporate Needs</span>
    </div>
  </div>
  <p class="page-no">02</p>
</section>

<section class="slide slide--why why">
  <span class="tag">WHY VEREDA 14</span>
  <h2 class="heading why__heading">Built for Productivity. Designed for Well-Being.</h2>
  <span class="rule"></span>
  <div class="features features--top">
    <div class="feature">
      <svg width="32" height="28" viewBox="0 0 32 28"><g class="s"><rect x="6" y="1" width="6" height="6"/><rect x="14" y="1" width="7" height="5"/><path d="M8 14h14v10H8zM10 14v-4h10v4M26 26V8M23 8h6l-1-3h-4zM1 18h6v8H1zM1 22h6M4 26v-4"/></g></svg>
      Fully Furnished &amp;<br>Move-in Ready
    </div>
    <div class="feature">
      <svg width="32" height="28" viewBox="0 0 32 28"><g class="s"><rect x="2" y="2" width="8" height="5"/><rect x="13" y="1" width="6" height="6"/><rect x="22" y="2" width="8" height="5"/><path d="M2 12h28v15H2zM11 12v15M21 12v15M21 18h9M5 16h3M14 18h4"/></g></svg>
      Designer Kitchens<br>Fully Equipped
    </div>
    <div class="feature">
      <svg width="32" height="28" viewBox="0 0 32 28"><g class="s"><path d="M2 10a20 20 0 0 1 28 0M6 14a14 14 0 0 1 20 0M10 18a8 8 0 0 1 12 0"/><circle cx="16" cy="23" r="2"/></g></svg>
      High-speed<br>Fiore Internet
    </div>
    <div class="feature">
      <svg width="40" height="28" viewBox="0 0 40 28"><g class="s"><rect x="1" y="2" width="38" height="11" rx="1"/><path d="M4 10h32M15 6h10M10 17c2 2-2 4 0 6M16 17c2 2-2 4 0 6M22 17c2 2-2 4 0 6M28 17c2 2-2 4 0 6"/></g></svg>
      Air Conditioning<br>&amp; Heating
    </div>
  </div>
  <div class="features features--bottom">
    <div class="feature">
      <svg width="24" height="28" viewBox="0 0 24 28"><g class="s"><rect x="2" y="1" width="20" height="26" rx="1"/><path d="M2 7h20M5 4h2M15 4h4"/><circle cx="12" cy="17" r="6"/><circle cx="12" cy="17" r="3.5"/></g></svg>
      Washing Machine<br>&amp; Laundry Area
    </div>
    <div class="feature">
      <svg width="28" height="28" viewBox="0 0 28 28"><g class="s"><path d="M12 2h14v25H12zM14 4l10 2v19l-10 1z"/><circle cx="21" cy="15" r="1"/><path d="M4 12l6-3 2 4-5 8-4 2zM3 6a4 4 0 0 1 5-2M2 3a7 7 0 0 1 7-2"/></g></svg>
      Smart Digital<br>Access
    </div>
    <div class="feature">
      <svg width="24" height="28" viewBox="0 0 24 28"><g class="s"><rect x="2" y="1" width="20" height="26" rx="1"/><rect x="4" y="3" width="16" height="19"/><circle cx="12" cy="7" r="2"/><path d="M6 17l2-5h8l2 5v3H6zM4 24h16"/></g></svg>
      Private on-site<br>Parking
    </div>
    <div class="feature">
      <svg width="24" height="28" viewBox="0 0 24 28"><g class="s"><path d="M3 27V5h12v22M15 11h6v16M1 27h22M6 8h2M10 8h2M6 12h2M10 12h2M6 16h2M10 16h2M6 20h2M10 20h2M17 15h2M17 19h2M17 23h2"/></g></svg>
      Approx. 85-95 m²<br>Per Apartment
    </div>
  </div>
  <p class="footer">© 2026 , Vereda14. All rights reserved.</p>
  <p class="page-no">03</p>
</section>

</body>
</html>
```